Business logo, card, letter head design needed

we run makeup & hair academy, also we have a retail shop in Prahran Vic. we ahve logo for our shop which (glomered tavi Cosmetics) but no logo yet for our academy, we hope can do a double side business card, front for the academy / back for the shop which we would like to use black back ground with our white round logo
Target Market(s)
16 - 40 female
Industry/Entity Type
Retail
Contact Information for Business Card
Kestrel Lane Beauty & Styling School (KLBSS)
Glomered Tavi Cosmetics
Dorotea Vranjesic
Director
47 Tallowby Rd. Prahran Vic 3181
E: dorotea@kestrelbeautyschool.com.au
M: 61-487302516
Academy web: www.kestrelbeautyschool.com.au
Shop web: www.glomeredtavi.com
Logo Text
Kestrel Lane Beauty & Styling School
Logo styles of interest
Wordmark Logo
Lettermark Logo
Look and feel

```html
<!DOCTYPE html>
<html lang="en">
<head>
<meta charset="utf-8">
<title>Kestrel Lane Beauty &amp; Styling School – Business Card</title>
<link href="https://fonts.googleapis.com/css2?family=Ubuntu:wght@400;500;700&display=swap" rel="stylesheet">
<style>
  :root {
    --stage: #e9e9e7;
    --card: #121212;
    --brand-blue: #1a9ad6;
    --white: #ffffff;
    --soft-white: #e6e6e6;
    --panel-light: #ededeb;
    --panel-dark: #000000;
    --ink-grey: #3a3a3a;
  }
  * { margin: 0; padding: 0; box-sizing: border-box; }
  html, body { width: 1200px; height: 1132px; overflow: hidden; }
  body {
    background: var(--stage);
    font-family: "Ubuntu", Arial, sans-serif;
    position: relative;
  }
  .card-stage {
    position: absolute; left: 0; top: 0; width: 1200px; height: 903px;
    background: radial-gradient(ellipse at center, #f6f6f4 0%, var(--stage) 75%);
  }
  .business-card {
    position: absolute; left: 210px; top: 228px; width: 780px; height: 446px;
    background: repeating-linear-gradient(135deg, #151515 0 3px, #101010 3px 6px);
    background-color: var(--card);
    box-shadow: 0 18px 40px rgba(0,0,0,.25);
    color: var(--white);
  }
  .brand-lockup {
    position: absolute; display: flex; align-items: center; gap: 14px;
  }
  .brand-mark {
    width: 46px; height: 46px; border-radius: 50%; flex: none;
  }
  .brand-name {
    font-weight: 500; color: var(--brand-blue); line-height: 1.05;
  }
  .business-card .brand-lockup { left: 48px; top: 52px; }
  .business-card .brand-mark { background: var(--soft-white); width: 58px; height: 58px; }
  .business-card .brand-name { font-size: 30px; width: 330px; }
  .holder { position: absolute; left: 430px; top: 230px; }
  .holder-name { font-size: 27px; font-weight: 500; }
  .holder-role { font-size: 16px; color: var(--soft-white); margin-top: 2px; }
  .contact-list { list-style: none; position: absolute; left: 400px; top: 318px; }
  .contact-list li {
    display: flex; align-items: center; gap: 10px;
    font-size: 17px; line-height: 25px; color: var(--soft-white);
  }
  .contact-list svg { width: 16px; height: 16px; flex: none; fill: var(--brand-blue); }
  .logo-panels { position: absolute; left: 0; top: 903px; width: 1200px; height: 229px; display: flex; }
  .logo-panel { position: relative; height: 100%; }
  .logo-panel.dark { width: 609px; background: var(--panel-dark); }
  .logo-panel.light { width: 591px; background: radial-gradient(ellipse at center, #fafaf9 0%, var(--panel-light) 80%); }
  .logo-panel .brand-lockup { left: 50%; top: 50%; transform: translate(-50%, -50%); }
  .logo-panel .brand-name { font-size: 22px; width: 250px; }
  .logo-panel.dark .brand-mark { background: var(--soft-white); }
  .logo-panel.light .brand-mark { background: var(--ink-grey); }
</style>
</head>
<body>
  <section class="card-stage">
    <article class="business-card">
      <div class="brand-lockup">
        <span class="brand-mark"></span>
        <span class="brand-name">Kestrel Lane Beauty &amp; Styling School</span>
      </div>
      <div class="holder">
        <p class="holder-name">Dorotea Vranjesic</p>
        <p class="holder-role">Director</p>
      </div>
      <ul class="contact-list">
        <li><svg viewBox="0 0 16 16"><path d="M8 1a5 5 0 0 0-5 5c0 4 5 9 5 9s5-5 5-9a5 5 0 0 0-5-5zm0 7a2 2 0 1 1 0-4 2 2 0 0 1 0 4z"/></svg>47 Tallowby Rd. Prahran Vic 3181</li>
        <li><svg viewBox="0 0 16 16"><path d="M1 4h14v9H1zM1 4l7 5 7-5" stroke="#121212" stroke-width="1.2"/></svg>dorotea@kestrelbeautyschool.com.au</li>
        <li><svg viewBox="0 0 16 16"><path d="M4 1l3 3-2 2c1 2 3 4 5 5l2-2 3 3-2 3C7 15 1 9 1 3z"/></svg>61-487302516</li>
        <li><svg viewBox="0 0 16 16"><circle cx="8" cy="8" r="7"/><path d="M1 8h14M8 1c-3 4-3 10 0 14M8 1c3 4 3 10 0 14" stroke="#121212" fill="none"/></svg>www.kestrelbeautyschool.com.au</li>
        <li><svg viewBox="0 0 16 16"><path d="M8 1l7 6h-2v8H3V7H1z"/></svg>www.glomeredtavi.com</li>
      </ul>
    </article>
  </section>
  <section class="logo-panels">
    <div class="logo-panel dark">
      <div class="brand-lockup">
        <span class="brand-mark"></span>
        <span class="brand-name">Kestrel Lane Beauty &amp; Styling School</span>
      </div>
    </div>
    <div class="logo-panel light">
      <div class="brand-lockup">
        <span class="brand-mark"></span>
        <span class="brand-name">Kestrel Lane Beauty &amp; Styling School</span>
      </div>
    </div>
  </section>
</body>
</html>
```